Orvath Commentary

Looking for a book and e book cover... (not ready to provide specs yet), but wanting to see creative designs.
This is a NEW commentary on the Book of Orvath. The essence of this book is as follows:
1) there are thousands of commentaries on the book of Orvath but all basically have the same interpretations - just personalized. This is clearly a very new interpretation.
2) Rather than a commentary that follows along using a "historical" approach, I have looked for the Messiah in the verses and thus come away with these new interpretations,
3) the book will / should be titled as follows:
Commentary of the Book of Orvath (top)
Creative image (center / field)
somewhere within image area - "Can you see my now..."
4) The "Can you see me now" statement is made by Kelmar with His image but not a traditional image of Him.
5) Because no one has looked for Him in Orvath this will be a play of contradiction - it might be an image of Him that one knows it is Kelmar but you still can not see Him,
6) I will attach a word file which captures some images from the website (belong to others) to give you some thought on what I like.. look forward to seeing (without restricting your creative process at all),
There is no rush on completing this at this time... this deadline can easily be extended to 2/15/23

```html
<!DOCTYPE html>
<html lang="en">
<head>
<meta charset="utf-8">
<title>New Interpretations – Book of Orvath</title>
<link href="https://fonts.googleapis.com/css2?family=Cinzel:wght@400;500&family=Cormorant+Garamond:wght@500&family=Frank+Ruhl+Libre:wght@700&display=swap" rel="stylesheet">
<style>
  :root {
    --ink-white: #ffffff;
    --ink-cream: #f3ebe0;
    --ink-soft: #ece6dc;
    --bg-top: #3c3c3e;
    --bg-grey: #58585a;
    --bg-deep: #241816;
    --bg-base: #0d0808;
    --parchment: #e6dccb;
    --parchment-shade: #c9b9a0;
    --robe-light: #cbbcab;
    --cloth-brown: #7d6651;
    --cloth-dark: #4a3a2e;
    --gold: #e7b75a;
    --gold-bright: #ffd98a;
  }
  html, body {
    margin: 0;
    padding: 0;
    width: 800px;
    height: 1200px;
    overflow: hidden;
    background: var(--bg-base);
  }
  .cover {
    position: relative;
    width: 800px;
    height: 1200px;
    overflow: hidden;
    background: linear-gradient(180deg, var(--bg-top) 0%, var(--bg-grey) 30%, #4a4542 60%, var(--bg-deep) 82%, var(--bg-base) 100%);
  }
  .cover-photo {
    position: absolute;
    left: 0;
    top: 330px;
    width: 800px;
    height: 720px;
    background:
      radial-gradient(ellipse 38% 22% at 72% 28%, var(--parchment) 0%, var(--parchment-shade) 55%, transparent 100%),
      radial-gradient(ellipse 30% 14% at 48% 22%, rgba(215, 195, 175, 0.9), transparent 100%),
      radial-gradient(ellipse 30% 20% at 12% 34%, var(--robe-light), transparent 100%),
      radial-gradient(ellipse 40% 22% at 30% 82%, var(--robe-light), transparent 100%),
      radial-gradient(ellipse 45% 30% at 40% 52%, var(--cloth-brown), transparent 100%),
      radial-gradient(ellipse 40% 30% at 85% 70%, var(--cloth-dark), transparent 100%),
      linear-gradient(180deg, transparent 0%, rgba(90, 75, 62, 0.8) 15%, rgba(90, 75, 62, 0.8) 75%, transparent 100%);
  }
  .light-streaks {
    position: absolute;
    inset: 0;
    width: 800px;
    height: 1200px;
  }
  .series {
    position: absolute;
    top: 36px;
    left: 0;
    width: 100%;
    margin: 0;
    text-align: center;
    font-family: "Cinzel", serif;
    font-weight: 500;
    font-size: 43px;
    line-height: 1;
    text-transform: uppercase;
    color: var(--ink-white);
  }
  .title {
    position: absolute;
    top: 94px;
    left: 0;
    width: 100%;
    margin: 0;
    text-align: center;
    font-family: "Cinzel", serif;
    font-weight: 400;
    text-transform: uppercase;
    color: var(--ink-white);
    line-height: 1;
  }
  .title-line { display: block; }
  .title-book {
    font-size: 128px;
    padding-left: 30px;
  }
  .title-of { font-size: 46px; }
  .title-name {
    font-size: 134px;
    margin-top: 8px;
  }
  .tagline {
    position: absolute;
    top: 902px;
    left: 0;
    width: 100%;
    margin: 0;
    text-align: center;
    color: var(--ink-soft);
  }
  .tagline-greek {
    display: block;
    font-family: "Cormorant Garamond", serif;
    font-weight: 500;
    font-size: 44px;
    line-height: 1;
  }
  .tagline-english {
    display: block;
    font-family: "Cinzel", serif;
    font-size: 31px;
    line-height: 1;
    margin-top: 0;
  }
  .tagline-hebrew {
    display: block;
    font-family: "Frank Ruhl Libre", serif;
    font-weight: 700;
    font-size: 37px;
    line-height: 1;
    margin-top: 2px;
    color: var(--ink-white);
  }
  .author {
    position: absolute;
    top: 1088px;
    left: 0;
    width: 100%;
    margin: 0;
    text-align: center;
    font-family: "Cinzel", serif;
    font-weight: 400;
    font-size: 54px;
    line-height: 1;
    text-transform: uppercase;
    color: var(--ink-cream);
  }
</style>
</head>
<body>
  <main class="cover">
    <div class="cover-photo" role="img" aria-label="Photograph of robed arms with fringed woven sleeves unrolling a parchment scroll marked with the name Kelmar and Hebrew letters, resting on a striped woven cloth"></div>

    <svg class="light-streaks" viewBox="0 0 800 1200" aria-hidden="true">
      <defs>
        <linearGradient id="streak" x1="0" x2="1" y1="0" y2="0">
          <stop offset="0" stop-color="#e7b75a" stop-opacity="0"/>
          <stop offset="0.35" stop-color="#e7b75a" stop-opacity="0.8"/>
          <stop offset="0.7" stop-color="#ffd98a" stop-opacity="0.6"/>
          <stop offset="1" stop-color="#e7b75a" stop-opacity="0"/>
        </linearGradient>
      </defs>
      <g fill="none" stroke="url(#streak)" stroke-linecap="round">
        <path d="M-20 70 C 160 20, 420 40, 820 110" stroke-width="10" opacity="0.7"/>
        <path d="M-20 150 C 180 110, 430 150, 820 130" stroke-width="14" opacity="0.6"/>
        <path d="M-20 210 C 200 170, 460 230, 820 210" stroke-width="18" opacity="0.75"/>
        <path d="M-20 290 C 220 250, 480 300, 820 260" stroke-width="10" opacity="0.5"/>
        <path d="M150 960 C 320 900, 520 920, 700 880" stroke-width="8" opacity="0.8"/>
        <path d="M180 975 C 340 930, 540 950, 720 900" stroke-width="5" opacity="0.7"/>
      </g>
    </svg>

    <p class="series">New Interpretations</p>

    <h1 class="title">
      <span class="title-line"><span class="title-book">Book</span> <span class="title-of">of</span></span>
      <span class="title-line title-name">Orvath</span>
    </h1>

    <p class="tagline">
      <span class="tagline-greek" lang="el">Xαν ψου σεε με νοω ...</span>
      <span class="tagline-english">Can You See Me Now ...</span>
      <span class="tagline-hebrew" lang="he" dir="rtl">אתה יכול לראות אותיעכשיו...</span>
    </p>

    <p class="author">Marcus L. Brennard</p>
  </main>
</body>
</html>
```